wardrobe/costume stylist needs good business card for own business

Hi:)

I'm wanting a business card for my company. I am a freelance stylist.

I do wardrobe/costume stylist to TV commercials; Films; Fashion and Lifestyle shoots.

I'd like a design based around my name Rosalind Pember written nicely, maybe a colour? Up to you?!

I've attached a couple of images of business cards I like
.... be creative and have fun!

Thank you :)
Updates

Reason: I was trying to get my new business card ready for before I headed overseas Friday morning but I don't think that was realistic so I'd like to extend the deadline to give time to the project. Thank you

Hi designers:) Thank you for all your designs, I've extended the deadline until Sunday, so there's a bit more time. I've attached 3 pictures of business cards which I quite like, please take a look to see if it can be of help in your process. I like the pale plain or patterned background with dark font and the dark plain or patterned background with the pale font the motifs the feminine fonts the plain fonts I like the idea of playing with a circle or some shape on one side of the card with my name or initials as in the picture I have on my post could you play around with this idea a bit please? Thank you all for the work you've done :) Rosa

Hi I am working overseas til Saturday night sorry for no feedback until I teturn Thanks :) Rosa

Hi designers, Thank you all so much for submitting your designs, I really appreciate your input into my project :) I'm sorry I didn't get to respond to some comments, and give feedback. I didn't back from being away until later than I expected, and the deadline had passed then, so apologies. Thanks to you all again for all your really good designs :) Rosa

Target Market(s)

I am a freelance stylist my target audience is producers, production companies, photographers, directors...

Industry/Entity Type

Business

Requirements
Must have
• Rosalind Pember
Stylist or Wardrobe Stylist

email rosapember@quillnet.co.nz
Mobile 0218846193

(Don't have to use the words 'email' and 'mobile')
Nice to have
• Would like it to be double sided
Like B & W
Like pale colour background with dark font or white font
Like dark colour background with pale font
Should not have
• I would prefer it not to incorporate pictures

```html
<!DOCTYPE html>
<html lang="en">
<head>
<meta charset="utf-8">
<title>Rosalind Pember — Stylist Business Card</title>
<link rel="stylesheet" href="https://fonts.googleapis.com/css2?family=Great+Vibes&family=Carlito&display=swap">
<style>
  :root {
    --canvas: #ffffff;
    --card-light: #ffffff;
    --pattern-light: #f1f1f1;
    --pattern-mid: #e4e4e4;
    --card-dark: #000000;
    --ink-dark: #111111;
    --ink-light: #ffffff;
  }
  html, body {
    margin: 0;
    padding: 0;
    width: 1200px;
    height: 1200px;
    overflow: hidden;
    background: var(--canvas);
  }
  .canvas {
    position: relative;
    width: 1200px;
    height: 1200px;
  }
  .card {
    position: absolute;
    top: 458px;
    width: 483px;
    height: 284px;
    overflow: hidden;
  }
  .card-front {
    left: 117px;
    background: var(--card-light);
  }
  .card-back {
    left: 600px;
    background: var(--card-dark);
  }
  .front-pattern {
    position: absolute;
    inset: 0;
    background:
      radial-gradient(ellipse at 30% 70%, var(--pattern-mid) 0%, transparent 55%),
      radial-gradient(ellipse at 75% 30%, var(--pattern-mid) 0%, transparent 50%),
      linear-gradient(135deg, var(--pattern-light), #fafafa 50%, var(--pattern-light));
  }
  .name-lockup {
    position: absolute;
    left: 0;
    top: 0;
    width: 100%;
    height: 100%;
  }
  .name-first,
  .name-last {
    position: absolute;
    font-family: "Great Vibes", cursive;
    font-size: 54px;
    line-height: 1;
    color: var(--ink-dark);
    white-space: nowrap;
  }
  .name-first {
    left: 106px;
    top: 82px;
  }
  .name-last {
    left: 172px;
    top: 118px;
  }
  .role-title {
    position: absolute;
    left: 268px;
    top: 166px;
    font-family: "Carlito", sans-serif;
    font-size: 21px;
    color: var(--ink-dark);
  }
  .contact {
    position: absolute;
    left: 0;
    right: 0;
    top: 118px;
    text-align: center;
    font-family: "Carlito", sans-serif;
    font-size: 18px;
    line-height: 25px;
    color: var(--ink-light);
  }
  .contact p { margin: 0; }
</style>
</head>
<body>
  <main class="canvas">
    <section class="card card-front">
      <div class="front-pattern" role="img" aria-label="Faint grey line-drawn folk pattern of paisleys, rosettes and geometric motifs"></div>
      <div class="name-lockup">
        <span class="name-first">Rosalind</span>
        <span class="name-last">Pember</span>
        <span class="role-title">Stylist</span>
      </div>
    </section>
    <section class="card card-back">
      <div class="contact">
        <p class="contact-email">rosapember@quillnet.co.nz</p>
        <p class="contact-phone">021 884 6193</p>
      </div>
    </section>
  </main>
</body>
</html>
```